Business Card Re-design

We are looking for a fresh bold look for general office business cards. We are a staffing agency that staffs industrial, coal mining, and clerical jobs.
Tag Line: We connect the RIGHT people with the RIGHT jobs.
Evansville Office: 2473 W. Tallow Creek Rd, Evansville, IN - 47308
p. 555.203.6180 f. 555.203.6195
Princeton Office: 264 S. Birch Ln, Princeton, IN - 47152
p. 555.319.2047 f. 555.203.6195
Absentee/Emergency 24hr Hotline 555.203.6172 opt.1
www.bluelanternworkforce.example

```html
<!DOCTYPE html>
<html lang="en">
<head>
<meta charset="utf-8">
<title>Blue Lantern Workforce – Office Business Cards</title>
<link href="https://fonts.googleapis.com/css2?family=Montserrat:wght@600;700&family=Questrial&display=swap" rel="stylesheet">
<style>
  :root {
    --page-bg: #e6e7e9;
    --card-black: #0a0b0d;
    --card-white: #ffffff;
    --panel-light: #eef0f4;
    --panel-warm: #f6f2f2;
    --panel-cool: #dfe3ea;
    --brand-navy: #17325a;
    --ink: #111111;
    --tagline-ink: #2a2a2a;
  }
  * { box-sizing: border-box; margin: 0; padding: 0; }
  html, body {
    width: 1200px; height: 1200px; overflow: hidden;
    background: var(--page-bg);
  }
  .sheet { position: relative; width: 1200px; height: 1200px; }

  .card {
    position: absolute;
    width: 880px; height: 537px;
    overflow: hidden;
    background: var(--card-black);
    font-family: "Questrial", "Century Gothic", sans-serif;
  }
  .card--princeton { left: 100px; top: 44px; }
  .card--evansville { left: 220px; top: 619px; }

  .card__photo {
    position: absolute; inset: 0;
    background:
      radial-gradient(ellipse at 70% 30%, var(--panel-cool) 0%, transparent 60%),
      linear-gradient(160deg, var(--panel-light) 0%, var(--panel-warm) 55%, var(--panel-light) 100%);
  }
  .card__shapes { position: absolute; inset: 0; }

  .card__rule {
    position: absolute; left: 77px; top: 0;
    width: 2px; height: 398px; background: var(--card-white);
  }
  .card__office {
    position: absolute; left: 89px; top: 62px;
    font-family: "Montserrat", sans-serif; font-weight: 700;
    font-size: 43px; line-height: 53px; color: var(--card-white);
  }
  .contact { position: absolute; left: 0; top: 0; width: 560px; }
  .contact__row {
    position: absolute; left: 0;
    display: flex; align-items: flex-start;
    color: var(--card-white); font-size: 22px; line-height: 27px;
    letter-spacing: 0.3px;
  }
  .contact__icon { width: 20px; height: 20px; margin-left: 43px; margin-right: 38px; margin-top: 3px; fill: var(--card-white); flex: none; }
  .contact__row--phone { top: 228px; }
  .contact__row--fax { top: 270px; }
  .contact__row--address { top: 306px; }
  .contact__row--web { top: 369px; }

  .hotline {
    position: absolute; left: 0; top: 455px; width: 410px; height: 64px;
    text-align: center; color: var(--ink);
    padding-top: 9px;
  }
  .hotline__label { font-size: 20px; line-height: 24px; }
  .hotline__number { font-family: "Montserrat", sans-serif; font-weight: 700; font-size: 19px; line-height: 24px; }

  .brand {
    position: absolute; left: 478px; top: 205px; width: 380px;
    display: flex; align-items: center; justify-content: center; gap: 16px;
  }
  .brand__square { width: 40px; height: 40px; background: var(--brand-navy); flex: none; }
  .brand__name {
    font-family: "Montserrat", sans-serif; font-weight: 700;
    font-size: 38px; line-height: 42px; color: var(--brand-navy);
    text-transform: uppercase; letter-spacing: 1px;
  }
  .tagline {
    position: absolute; left: 478px; top: 354px; width: 380px;
    text-align: center; font-size: 13.5px; color: var(--tagline-ink);
  }
</style>
</head>
<body>
<svg width="0" height="0" style="position:absolute" aria-hidden="true">
  <defs>
    <symbol id="icon-phone" viewBox="0 0 24 24"><path d="M6.6 2.5l3 3.3-2 2.3c1.3 2.8 3.4 5 6.3 6.4l2.3-2 3.3 3-2 3.5C10 18.5 5.5 14 3 6.5z"/></symbol>
    <symbol id="icon-fax" viewBox="0 0 24 24"><path d="M1 8h4v14H1zM7 9h15v13H7zM10 2h9v6h-9zM10 12h3v2h-3zm5 0h3v2h-3zm-5 4h3v2h-3zm5 0h3v2h-3z"/></symbol>
    <symbol id="icon-home" viewBox="0 0 24 24"><path d="M12 2l11 10h-3v10h-6v-6h-4v6H4V12H1z"/></symbol>
    <symbol id="icon-globe" viewBox="0 0 24 24"><path d="M12 1a11 11 0 100 22 11 11 0 000-22zm0 2a9 9 0 016.5 2.8l-2.5.7-1 2 2 2-1 3h-3l-2-2 1-3-2-2 1-3zm-7 5l3 1 1 3 3 2-1 3 2 3v1A9 9 0 015 8z"/></symbol>
  </defs>
</svg>

<main class="sheet">
  <article class="card card--princeton">
    <div class="card__photo" role="img" aria-label="Faded photograph of industrial workers in soft blue and warm grey tones"></div>
    <svg class="card__shapes" viewBox="0 0 880 537" aria-hidden="true">
      <polygon points="0,0 557,0 432,537 0,537" fill="var(--card-black)"/>
      <polygon points="0,455 451,455 436,519 0,519" fill="var(--card-white)"/>
    </svg>
    <div class="card__rule"></div>
    <h2 class="card__office">Princeton<br>Office</h2>
    <div class="contact">
      <div class="contact__row contact__row--phone"><svg class="contact__icon"><use href="#icon-phone"/></svg>555.319.2047</div>
      <div class="contact__row contact__row--fax"><svg class="contact__icon"><use href="#icon-fax"/></svg>555.203.6195</div>
      <div class="contact__row contact__row--address"><svg class="contact__icon"><use href="#icon-home"/></svg><span>264 S. Birch Ln, Princeton,<br>IN - 47152</span></div>
      <div class="contact__row contact__row--web"><svg class="contact__icon"><use href="#icon-globe"/></svg>www.bluelanternworkforce.example</div>
    </div>
    <div class="hotline">
      <p class="hotline__label">Absentee/Emergency 24hr Hotline</p>
      <p class="hotline__number">555.203.6172 opt.1</p>
    </div>
    <div class="brand"><span class="brand__square"></span><span class="brand__name">Blue Lantern<br>Workforce</span></div>
    <p class="tagline">We connect the RIGHT people with the RIGHT jobs.</p>
  </article>

  <article class="card card--evansville">
    <div class="card__photo" role="img" aria-label="Faded photograph of industrial workers in soft blue and warm grey tones"></div>
    <svg class="card__shapes" viewBox="0 0 880 537" aria-hidden="true">
      <polygon points="0,0 557,0 432,537 0,537" fill="var(--card-black)"/>
      <polygon points="0,455 451,455 436,519 0,519" fill="var(--card-white)"/>
    </svg>
    <div class="card__rule"></div>
    <h2 class="card__office">Evansville<br>Office</h2>
    <div class="contact">
      <div class="contact__row contact__row--phone"><svg class="contact__icon"><use href="#icon-phone"/></svg>555.203.6180</div>
      <div class="contact__row contact__row--fax"><svg class="contact__icon"><use href="#icon-fax"/></svg>555.203.6195</div>
      <div class="contact__row contact__row--address"><svg class="contact__icon"><use href="#icon-home"/></svg><span>2473 W. Tallow Creek Rd,<br>Evansville, IN - 47308</span></div>
      <div class="contact__row contact__row--web"><svg class="contact__icon"><use href="#icon-globe"/></svg>www.bluelanternworkforce.example</div>
    </div>
    <div class="hotline">
      <p class="hotline__label">Absentee/Emergency 24hr Hotline</p>
      <p class="hotline__number">555.203.6172 opt.1</p>
    </div>
    <div class="brand"><span class="brand__square"></span><span class="brand__name">Blue Lantern<br>Workforce</span></div>
    <p class="tagline">We connect the RIGHT people with the RIGHT jobs.</p>
  </article>
</main>
</body>
</html>
```